KT Prime Motion personal training needs a new Business Card design for 2016

Business Card design:
Our current business card is very plain
We are bringing on our first team member next year and thought its a perfect time to have a new face lift for our company!

We are a Personal Training business "KT Prime Motion" who specializes in strength and conditioning / weightloss training,
We also run a yearly Bootcamp called "Ferocity Drillcamps", this is our Logo Design which we are looking for

The pink and blue in the logo are our business colours, how ever we don't want those colours to heavily dominate the card.

We are looking for a business card which is eye catching, and creative.

I am open to suggestions and any designs :)

Logo Design:

For our Logo Design we are looking for a bright, energetic logo, preferably a word logo which portrays strength and high intensity
If it has icon's etc in it thats fine again im open for suggestions :)
The Logo Design is for our Bootcamp which runs yearly
The bootcamp is called "Ferocity Drillcamp"

Target Market(s)

Age 20-40
Individuals who want to look great and have more energy

Industry/Entity Type

Business

Contact Information for Business Card

On the front
KT Prime Motion Doriel Maxton Personal Training / Bootcamps / Pilates / Nutrition Healthy mind, Healthy body, Ultimate lifestyle < our slogan
Icons for the following
Email:
Mobile:
Facebook:
Instagram:

On the back we would like to include somewhere
"Show this card to receive 50% off your first 30min pt session"
"Valid to one user only"

Logo Text

Ferocity Drillcamp

Font styles to use
Serif

Colors
e34197
0255a3
000000
ffffff

Requirements
Must have
• - Icons for instagram, facebook, email and mobile phone
• - Slogan: Healthy mind, Healthy body, Ultimate lifestyle
• - What we offer: Personal Training , Bootcamps, Pilates, Nutrition
• - Logo
• -
Nice to have
• - Our 50% offer on the back
• - a place for a photo
Should not have
• - Pink and Blue everywhere

```html
<!DOCTYPE html>
<html lang="en">
<head>
<meta charset="utf-8">
<title>KT Prime Motion – Business Card</title>
<link href="https://fonts.googleapis.com/css2?family=Source+Sans+3:wght@400;600;700&display=swap" rel="stylesheet">
<style>
  :root {
    --pink: #e34197;
    --blue: #0255a3;
    --ink-blue: #1a4f9c;
    --white: #ffffff;
    --backdrop: #161616;
    --rule: #d9d9d9;
  }
  * { box-sizing: border-box; margin: 0; padding: 0; }
  html, body {
    width: 1200px; height: 900px; overflow: hidden;
    background: var(--backdrop);
    font-family: "Source Sans 3", "Myriad Pro", sans-serif;
  }
  .card {
    position: absolute; top: 306px; height: 271px;
    background: var(--white); border-radius: 12px;
  }
  .card--front { left: 149px; width: 439px; }
  .card--back { left: 608px; width: 441px; }

  .divider {
    position: absolute; top: 58px; height: 138px; width: 1px;
    background: var(--rule);
  }
  .card--front .divider { left: 235px; }
  .card--back .divider { left: 229px; }

  .brand {
    position: absolute; display: flex; flex-direction: column;
    align-items: center; gap: 8px; text-align: center;
  }
  .brand__dot {
    width: 46px; height: 46px; border-radius: 50%; background: var(--blue);
  }
  .brand__name {
    color: var(--blue); font-weight: 700; font-size: 20px;
    line-height: 1.05; text-transform: uppercase;
  }
  .card--front .brand { left: 30px; top: 80px; width: 186px; }
  .card--back .brand { left: 36px; top: 62px; width: 170px; }

  .holder {
    position: absolute; left: 256px; top: 69px;
    color: var(--pink); font-size: 17px; font-weight: 600;
  }
  .contacts {
    position: absolute; left: 256px; top: 110px; list-style: none;
  }
  .contacts li {
    display: flex; align-items: center; height: 18.3px;
    color: var(--blue); font-size: 13px;
  }
  .contacts svg { width: 10px; height: 10px; margin-right: 13px; fill: var(--pink); }

  .slogan {
    position: absolute; left: 0; right: 0; top: 214px; text-align: center;
    color: var(--pink); font-size: 15px; font-weight: 600;
  }
  .slogan .sep { color: var(--blue); margin: 0 5px; font-weight: 400; }

  .offer-title {
    position: absolute; left: 259px; top: 71px;
    color: var(--blue); font-size: 16px; font-weight: 600;
  }
  .services { position: absolute; left: 259px; top: 101px; list-style: none; }
  .services li {
    display: flex; align-items: center; height: 20px;
    color: var(--blue); font-size: 14.5px; font-weight: 600;
  }
  .services li::before {
    content: ""; width: 9px; height: 9px; border-radius: 50%;
    background: var(--pink); margin-right: 6px;
  }

  .promo {
    position: absolute; left: 0; right: 0; top: 210px; text-align: center;
    font-size: 12.5px; line-height: 16px;
  }
  .promo__deal { color: var(--blue); }
  .promo__terms { color: var(--pink); }
</style>
</head>
<body>

<section class="card card--front">
  <div class="brand">
    <span class="brand__dot"></span>
    <span class="brand__name">KT Prime Motion</span>
  </div>
  <span class="divider"></span>
  <h1 class="holder">Doriel Maxton</h1>
  <ul class="contacts">
    <li><svg viewBox="0 0 10 10"><path d="M2 0.5 L3.8 2.6 L2.8 3.8 C3.5 5.2 4.8 6.5 6.2 7.2 L7.4 6.2 L9.5 8 L8.3 9.5 C4.5 9 1 5.5 0.5 1.7 Z"/></svg>555 014 2093</li>
    <li><svg viewBox="0 0 10 10"><path d="M0.5 2 H9.5 V8.5 H0.5 Z M1.2 2.7 L5 5.6 L8.8 2.7" /></svg>hello@ktprimemotion.net</li>
    <li><svg viewBox="0 0 10 10"><rect x="2" y="2" width="6" height="6"/></svg>ktprime-social.net</li>
    <li><svg viewBox="0 0 10 10"><rect x="2" y="2" width="6" height="6"/></svg>ktprime-photos.net</li>
  </ul>
  <p class="slogan">Healthy Mind<span class="sep">|</span>Healthy Body<span class="sep">|</span>Ultimate Lifestyle</p>
</section>

<section class="card card--back">
  <div class="brand">
    <span class="brand__dot"></span>
    <span class="brand__name">KT Prime Motion</span>
  </div>
  <span class="divider"></span>
  <h2 class="offer-title">What we offer</h2>
  <ul class="services">
    <li>Personal Training</li>
    <li>Bootcamps</li>
    <li>Pilates</li>
    <li>Nutrition</li>
  </ul>
  <div class="promo">
    <p class="promo__deal">Show this card to receive 50% off your first 30min pt session</p>
    <p class="promo__terms">Valid to one user only</p>
  </div>
</section>

</body>
</html>
```